Personal Care and Home care ingredients Brochure

We need a flyer or brochure of the of chemicals we distribute for the manufacturing of personal care products such as shampoos, liquid soaps, creams, lotions, conditioners, hand sanitizer, Hair Jellys, etc and for Home care products such as, liquid soaps, desinfectants, cleaners, stain removers,etc.
The idea is to send this pdf brochure via email and companies feel very confortable with the impression it gives. We want to call attention.
Target Market(s)
Companies that manufactures cosmetics, personal care products and home care products.
Colors
Designer to choose colors to be used in the design.
Requirements
Must have
- Images that refers to the skin, hair, cleaning, washing

```html
<!DOCTYPE html>
<html lang="es">
<head>
<meta charset="utf-8">
<title>Novara Química – Cuidado Personal y del Hogar</title>
<link href="https://fonts.googleapis.com/css2?family=Open+Sans:wght@400;600;700;800&display=swap" rel="stylesheet">
<style>
:root{
  --teal:#2f8c79;
  --teal-dark:#246f60;
  --ink:#2b2b2b;
  --muted:#555;
  --rule:#9aa3a0;
  --grey-head:#8d9190;
  --page:#f2f2f2;
  --white:#ffffff;
  --badge:#d9dcdb;
}
*{box-sizing:border-box;margin:0;padding:0}
html,body{width:1200px;height:2775px;overflow:hidden}
body{background:var(--page);font-family:"Open Sans",Arial,sans-serif;color:var(--ink);position:relative}
.sheet{position:absolute;left:86px;top:62px;width:1022px;height:2660px;background:var(--white);overflow:hidden}
.abs{position:absolute}

/* hero */
.hero{left:0;top:0;width:1022px;height:564px;background:linear-gradient(180deg,#cfe6f3 0%,#a7d2ec 35%,#4fa6d8 58%,#2f86c4 70%,#8fc96a 88%,#5aa24a 100%)}
.brand{left:58px;top:36px;display:flex;align-items:center;gap:14px}
.brand-mark{width:46px;height:46px;background:var(--teal);border-radius:6px}
.brand-name{font-weight:800;font-size:30px;color:#1f3f5a;letter-spacing:1px;line-height:1}
.hero-title{left:30px;top:318px;font-weight:700;font-size:42px;line-height:50px;color:#1b2a33}
.hero-sub{left:30px;top:430px;font-size:24px;line-height:34px;color:#1b2a33;width:970px}

/* bars */
.bar{background:var(--teal);color:var(--white);font-weight:700}
.bar small{display:block;font-weight:400;font-size:18px}
.intro-bar{left:0;top:574px;width:520px;height:66px;padding:6px 16px;font-size:22px;line-height:27px}
.soft-bar{left:0;top:996px;width:520px;height:62px;padding:6px 16px;font-size:22px;line-height:26px}

.photo{background:linear-gradient(135deg,#e9d7d3,#c98c8c 55%,#b84b6a)}
.photo-hands{left:546px;top:574px;width:476px;height:348px}
.photo-baby{left:546px;top:938px;width:476px;height:384px;background:linear-gradient(135deg,#f1ece6,#e6cdb8 55%,#c9a48b)}
.photo-kitchen{left:512px;top:1716px;width:500px;height:410px;background:linear-gradient(135deg,#f3f4ef,#d9e6c9 50%,#a9c0a0)}

.copy{font-size:15px;line-height:21px;color:var(--muted)}
.intro-copy{left:16px;top:652px;width:500px}
.feature{left:16px;width:504px}
.feature h4{font-weight:400;font-size:21px;color:var(--ink);border-top:1px solid var(--rule);padding-top:4px}
.feature p{font-size:14px;color:var(--muted);line-height:19px}
.f1{top:806px}.f2{top:856px}.f3{top:908px}
.soft-copy{left:16px;top:1072px;width:504px}
.soft-copy h4{font-size:19px;font-weight:700;border-top:1px solid var(--rule);padding-top:8px;margin-bottom:2px}
.soft-copy h5{font-size:19px;font-weight:700;border-top:1px solid var(--rule);padding-top:8px;margin-top:14px}
.soft-copy p{font-size:15px;line-height:21px;color:var(--muted)}

/* MES */
.mes-band{left:0;top:1336px;width:1022px;height:94px;padding:22px 36px;font-size:22px;line-height:24px}
.mes-bracket{left:0;top:1440px}
.mes-title{left:0;top:1432px;width:1022px;text-align:center;font-weight:700;font-size:38px;line-height:48px;color:var(--teal)}
.mes-title span{background:var(--white);padding:0 14px}
.swap-head{top:1480px;height:32px;background:var(--grey-head);color:var(--white);font-weight:600;font-size:18px;padding:4px 14px}
.swap-a{left:0;width:470px}.swap-b{left:530px;width:470px}
.swap-list{top:1520px;font-size:14px;line-height:19px}
.swap-list h4{font-size:14px;font-weight:700;margin-bottom:2px}
.swap-list ul{padding-left:30px}
.list-a{left:58px;width:460px}.list-b{left:588px;width:420px}
.divider{left:0;top:1682px;width:1022px;height:3px;background:var(--rule)}

.notes{left:22px;top:1702px;width:468px;font-size:14px;line-height:18px}
.notes ul{padding-left:18px}
.notes li{margin-bottom:3px}
.notes h4{font-size:17px;font-weight:800;margin:10px 0 4px}

/* products */
.products-bar{left:0;top:2150px;width:1022px;height:30px;padding:3px 30px;font-size:18px;line-height:24px}
.col{top:2192px;font-size:14px;line-height:19px}
.col h4{font-size:14px;font-weight:800}
.col .gap{margin-top:20px}
.c1{left:40px;width:280px}.c2{left:327px;width:350px}.c3{left:679px;width:330px}

.allies-bar{left:0;top:2530px;width:1022px;height:24px;text-align:center;font-size:12px;line-height:24px}
.allies{left:70px;top:2568px;display:flex;gap:30px;align-items:center}
.allies span{display:block;height:42px;background:var(--badge);border-radius:4px}
.foot-bar{left:0;top:2632px;width:1022px;height:22px}
</style>
</head>
<body>
<main class="sheet">
  <section class="abs hero" role="img" aria-label="Ropa blanca tendida al sol sobre agua salpicando y césped verde"></section>
  <div class="abs brand"><span class="brand-mark"></span><span class="brand-name">NOVARA QUÍMICA</span></div>
  <h1 class="abs hero-title">Cuidado Personal &amp;<br>Cuidados en el hogar Solución</h1>
  <p class="abs hero-sub">champús, jabones líquidos, cremas, lociones, acondicionadores, desinfectantes de manos, Jellys para el cabello, desinfectantes, limpiadores, quitamanchas</p>

  <div class="abs bar intro-bar">Nueva linea de PALMESTRA<br>Sulfonatos de Ester Metílico (MES)</div>
  <p class="abs copy intro-copy">El PALMESTRA es un surfactante iónico utilizado como ingrediente activo en detergentes.<br>Su principal uso es como substituto del surfactante universalmente utilizado, LAS o alquil sulfonatos lineales en las formulas de los detergentes. Esta hecho de recursos naturales renovables, lo cual le da un excelente biodegradabilidad, y muestra una mejor detergencia y tolerancia a la dureza durante el lavado.</p>
  <div class="abs feature f1"><h4>Excelente Detergencia:</h4><p>Desempeño superior en aguas con alta dureza vs las alternativa</p></div>
  <div class="abs feature f2"><h4>Cuidado de la Ropa:</h4><p>Excelente compatibilidad con Enzimas.</p></div>
  <div class="abs feature f3"><h4>Versatilidad para usar en Polvos y Líquidos:</h4><p>minimiza el uso de ingredientes SKU en productos de consumo masivo. Aplicación en un amplio rango de formulaciones.</p></div>

  <div class="abs photo photo-hands" role="img" aria-label="Manos enjabonadas con espuma sobre un recipiente rosa"></div>
  <div class="abs photo photo-baby" role="img" aria-label="Madre abrazando a su bebé de piel suave"></div>

  <div class="abs bar soft-bar">PALMESTRA<small>Seguridad y Suavidad</small></div>
  <div class="abs soft-copy">
    <h4>IMPARTE EL BALANCE PERFECTO</h4>
    <p>Suave a la piel y a los textiles.</p>
    <h5>El PALMESTRA es un surfactante mas verde.<br>Huella mas verde</h5>
    <p>Eco-amigable<br>Hecho de fuentes renovables<br>Sustentable<br>Biodegradable</p>
  </div>

  <div class="abs bar mes-band">PALMESTRA<small>Sulfonatos de Ester Metílico (MES)</small></div>
  <svg class="abs mes-bracket" width="1022" height="40" viewBox="0 0 1022 40"><path d="M236 40V16H786V40" fill="none" stroke="#8d9190" stroke-width="2"/></svg>
  <div class="abs mes-title"><span>MES</span></div>
  <div class="abs swap-head swap-a">Reemplazo de LABSA</div>
  <div class="abs swap-head swap-b">Reemplazo de SLES</div>
  <div class="abs swap-list list-a">
    <h4>LAVAPLATOS LIQUIDOS Y DETERGENTES<br>LIQUIDOS DE LAVANDERIA</h4>
    <ul><li>Más suave para la piel</li><li>Ingrediente Alternativo a Productos derivados del Petróleo</li><li>Mejor detergencia en Agua Dura.</li><li>Mejor remoción de manchas de aceite.</li><li>Uso de productos naturales derivados de la palma.</li></ul>
  </div>
  <div class="abs swap-list list-b">
    <h4>LAVAPLATOS LIQUIDOS / DETERGENTES<br>LIQUIDOS / JABANO DE TOCADOR LIQUIDO</h4>
    <ul><li>Menor costo de materia prima por unidad activa.</li><li>Desempeño similar</li><li>Suavidad similar al SLES</li></ul>
  </div>
  <div class="abs divider"></div>

  <div class="abs notes">
    <ul>
      <li>El MES no necesita neutralizacion, y al diluir la solicion ya esta activa.</li>
      <li>Se recomienda 30-50% de LABSA y no un reemplazo total para lograr un efecto - sinergístico.</li>
      <li>Comparado con el LABSA, el MES es mas suave para la piel, un tiene efecto de limpieza mas fuerte sobre manchas de grasas vegetales/oleosas y un mayor poder de detergencia en aguas con alto contenido de dureza.</li>
    </ul>
    <h4>RECOMENDACIONES GENERALES</h4>
    <ul>
      <li>Si se requiere que el liquido final lavaplatos/detergente sea transparente o cristalino, el maximo contenido de MES no debe ser mas de 5%.</li>
      <li>A pesar que es posible reemplazar totalmente el LAS o LABSA, se recomienda la presencia de mas surfactantes para buscar un mejor efecto sinergistico.</li>
      <li>MES no debe ser expuesto a pH menor de 5 o mayor de 9 por mas de 24 horas porque se degrada.</li>
      <li>El uso de MES en productos liquidos requiere una dosis de ajuste de electrolito (Sal) para alcanzar la viscosidad deseada.</li>
    </ul>
  </div>
  <div class="abs photo photo-kitchen" role="img" aria-label="Padre e hija lavando platos en una cocina luminosa"></div>

  <div class="abs bar products-bar">PRODUCTOS PARA CUIDADO PERSONAL Y CUIDADO DEL HOGAR</div>
  <div class="abs col c1">
    <h4>ALCOHOLES GRASOS</h4>Alcohol Cetílico<br>Alcohol Ceto-Estearílico<br>Alcohol Estearílico<br>Alcohol Laurico<br>Alcohol Miristílico
    <h4 class="gap">ACIDOS GRASOS</h4>Acido Estearico Triple Prensado<br>Acido Oleico<br>Acido Palmítico
    <h4 class="gap">BUTIL GLICOL<br>GLICERINA<br>PROPILEN GLICOL<br>TRIETANOLAMINA</h4>
  </div>
  <div class="abs col c2">
    <h4>ESTERES</h4>Estearato de Glicol (EGS)<br>Diestearato de Glicol (EGDS)<br>Triglicérido Caprílico / Caprico<br>Palmitato de etil Hexilo (EHP)<br>Palmitato de Isopropilo (IPP)<br>Palmitato de Miristato (IPM)
    <h4 class="gap">SURFACTANTES ANIONICOS</h4>Sulfonatos de Ester Metílico (MES)<br>Viruta de Jabon ( Soap Noodles / Soap Bases)<br>Lauril Eter Sulfato de Sodio (SLES)<br>Lauril Sulfato de Sodio (SLS)<br>Lauril Sulfosuccinato de Sodio (Surfactante Suave)<br>Base para Jabones Sinteticos (Syndets)<br>Acido Alquilbenceno Sulfonico Lineal (LABSA)
  </div>
  <div class="abs col c3">
    <h4>AMIDAS</h4>Cocoamida DEA<br>Cocoamida MEA<br>Cocoamido propil Betaina (CAPB)
    <h4 class="gap">VITAMINA E</h4>Tocotrienoles
    <h4 class="gap">FRAGANCIAS DE AROMATERRA IBÉRICA</h4>Para cuidado Personal<br>Para cuidado del Hogar
  </div>

  <div class="abs bar allies-bar">NUESTROS ALIADOS COMERCIALES:</div>
  <div class="abs allies" aria-label="Aliados comerciales">
    <span style="width:120px"></span><span style="width:80px"></span><span style="width:120px"></span><span style="width:110px"></span><span style="width:130px"></span><span style="width:130px"></span>
  </div>
  <div class="abs bar foot-bar"></div>
</main>
</body>
</html>
```